Design a cover that embodies the concept of healing by Walking Out of Sorrow

Subtitle: How to use tapping, applied kinesiology, and Chinese medicine to heal your body, free your mind and live in peace.

Tapping (Emotional Freedom Technique) is a modern mix of psychology and Chinese medicine that helps people to release the emotions they have inside that are contributing to the depression and anxiety they feel. Applied kinesiology or muscle testing is a biofeedback tool which helps to extract information from the body that can help people to profoundly heal. It can be used to determine whether heavy metals, heavy chemicals, food sensitivities or pathogens are causing the body problems. It can also be used to determine which supplements can help someone heal. This tool also can be used to identify emotions and memories that are also causing someone problems. Lastly, Chinese medicine uses food therapy, herbal formulas, meditation, tai chi (meditative movement), cupping and other tools to help people to be free of depression. This book is written to be information but also details my own personal journey of how I was able to heal from 11 years of heavy depression through the use of these tools.

The heart of the book is about emotional release, emotional freedom and emotional healing. You can surrender, release or let go of emotions and feel better very quickly. This certainly was my experience.

I would like the front and back cover to each be 8.5" x 5.5". I still have to get an ISBN number for the back page as well. Here is the text that I would like on the back cover for now: Millions of people feel the pain, loneliness, and agony of anxiety and depression every day. Many turn to Western medicine in the hopes that a pill will ease the pain and make the problem go away. Oftentimes, this only makes matters worse and doesn’t address the root cause. No one should have to struggle like this when natural answers exist that can address the physical, energetic, emotional, or spiritual causes of anxiety and depression. For 11 long years, Dr. Neil personally struggled with heavy depression until he discovered answers that helped him to completely heal. Walking Out of Sorrow is a guide that will help you discover - The two root physical causes of depression and exactly what to do to start healing today - How the negative emotions we have stored within from trauma and bad experiences can drive depression - Tools from Chinese medicine, applied kinesiology, and tapping to help you free your mind and live in peace - An actionable plan to help you let go of the pain, suffering, and negative emotions from your past Whether you feel depressed and anxious or know someone who struggles with these issues, Walking Out of Sorrow will transform how you think about depression and will give you the tools to heal so that you can be free and live in peace. Dr. Neil Prentor is a board-certified acupuncture physician licensed in the state of Florida. He received his training at the Marlow Institute of Holistic Practice. He also graduated with a master’s degree in counseling and psychology from Ashcombe Seminary of Theology. His mission is to help people transform their health and improve the quality of their life naturally. He lives in Orlando, FL where he runs a holistic medical clinic called Kestrel Wellness Center. www.drneilprentor.example Instagram: drneilprentor Facebook: kestrelwellnesscenter

Target Market(s)

Those who suffer from depression and anxiety and want to heal naturally

Industry/Entity Type

Health And Wellness

Requirements
Must have
• My picture should be small and go on the back cover next to the information about me. The front cover would be all graphical. Thank you. On the front cover my name should be posted as "Dr. Neil Prentor, AP, MA"

```html
<!DOCTYPE html>
<html lang="en">
<head>
<meta charset="utf-8">
<title>Walking Out of Sorrow — Cover Spread</title>
<link href="https://fonts.googleapis.com/css2?family=Bebas+Neue&family=Oswald:wght@400;500&family=IM+Fell+English:ital@1&family=Special+Elite&family=Oxygen:wght@400;700&display=swap" rel="stylesheet">
<style>
  :root {
    --page-bg: #f1f1f1;
    --ink-black: #0b0b0b;
    --gold: #f2b01e;
    --gold-deep: #d98c0a;
    --title-yellow: #f7d57a;
    --cream: #f3ecdc;
    --orange-1: #ffd7a6;
    --orange-2: #f8a53a;
    --orange-3: #f07e12;
    --strip-orange: #fbc86a;
    --strip-red: #d8260f;
    --name-grey: #c9c9c9;
    --pink: #ff2e9a;
    --back-bg: #0e0c12;
    --back-violet: #2a1738;
    --back-text: #e6e2dc;
    --rule-red: #8a1010;
    --spine-purple: #6a2aa0;
  }
  * { box-sizing: border-box; margin: 0; padding: 0; }
  html, body { width: 1200px; height: 858px; overflow: hidden; background: var(--page-bg); }
  .spread {
    position: absolute; left: 83px; top: 39px;
    width: 1034px; height: 780px; display: flex;
    box-shadow: 0 6px 24px rgba(0,0,0,.18);
  }

  /* Back cover */
  .back-cover {
    position: relative; width: 505px; height: 780px; overflow: hidden;
    background: radial-gradient(ellipse at 30% 75%, var(--back-violet), var(--back-bg) 60%);
    color: var(--back-text);
  }
  .back-header {
    position: relative; height: 112px;
    background: linear-gradient(#141418, #1b2a33);
    border-bottom: 5px solid var(--rule-red);
  }
  .back-kicker {
    position: absolute; top: 12px; left: 120px;
    font: 20px "Bebas Neue", sans-serif; letter-spacing: 3px; color: var(--pink);
  }
  .back-name {
    position: absolute; left: 10px; top: 30px;
    font: 500 74px/1 "Oswald", sans-serif; letter-spacing: -1px; color: #f3f3f3;
    white-space: nowrap;
  }
  .back-name small { font-size: 22px; letter-spacing: 0; margin-right: 4px; }
  .back-body {
    position: absolute; left: 14px; right: 16px; top: 124px; height: 560px; overflow: hidden;
    font: italic 12.6px/18px "IM Fell English", serif; text-align: justify;
  }
  .back-body p + p { margin-top: 6px; }
  .author-portrait {
    float: left; width: 175px; height: 232px; margin: 2px 12px 0 -14px;
    background: linear-gradient(160deg, #6b4a3a, #c89d80 40%, #efe6cf 75%);
  }
  .author-site { display: block; margin-top: 4px; }
  .back-footer {
    position: absolute; left: 0; right: 0; bottom: 0; height: 92px;
    background: linear-gradient(#2a0406, #120203);
    border-top: 5px solid var(--rule-red);
    padding: 16px 16px;
    font: 18px/30px "Oxygen", sans-serif; color: #d8d8d8; letter-spacing: .5px;
  }
  .social { display: flex; align-items: center; gap: 10px; }
  .social-mark { width: 20px; height: 20px; background: #d8d8d8; border-radius: 4px; }

  /* Spine */
  .spine {
    position: relative; width: 24px; height: 780px;
    background: linear-gradient(90deg, var(--gold-deep), var(--gold), var(--gold-deep));
  }
  .spine-text {
    position: absolute; left: 50%; top: 16px;
    transform: translateX(-50%); writing-mode: vertical-rl;
    white-space: nowrap; color: var(--spine-purple);
  }
  .spine-author { font: 11px "Special Elite", serif; letter-spacing: 1px; }
  .spine-title { margin-top: 30px; font: 18px "Bebas Neue", sans-serif; letter-spacing: 3px; }

  /* Front cover */
  .front-cover {
    position: relative; width: 505px; height: 780px; overflow: hidden;
    background: var(--ink-black);
    border-top: 8px solid var(--gold); border-bottom: 8px solid var(--gold);
  }
  .front-head { height: 196px; padding: 26px 14px 0; text-align: center; }
  .front-title {
    font: 56px/1 "Bebas Neue", sans-serif; color: var(--title-yellow); letter-spacing: .5px;
    white-space: nowrap;
    padding-bottom: 8px; border-bottom: 2px solid var(--gold);
  }
  .front-subtitle {
    margin-top: 14px; font: 14px/25px "Special Elite", serif; color: var(--cream);
    white-space: nowrap;
  }
  .front-art {
    position: relative; height: 438px;
    background:
      radial-gradient(ellipse at 72% 22%, #fff2e0 0, transparent 45%),
      linear-gradient(180deg, var(--orange-1) 0%, var(--orange-2) 55%, var(--orange-3) 100%);
  }
  .art-word { position: absolute; font-family: "Oswald", sans-serif; font-weight: 500; color: #fff; line-height: 1; white-space: nowrap; text-shadow: 0 1px 2px rgba(160,70,0,.35); }
  .art-emotional { left: 88px; top: 100px; font-size: 50px; writing-mode: vertical-rl; transform: rotate(180deg); letter-spacing: -1px; }
  .art-learn { left: 54px; top: 360px; font-size: 42px; }
  .art-release { right: 6px; top: 240px; font-size: 38px; }
  .art-freedom { right: 4px; top: 280px; font-size: 62px; }
  .art-healing { right: 6px; top: 350px; font-size: 40px; }
  .front-strip {
    height: 70px; background: var(--strip-orange);
    border-bottom: 6px solid var(--orange-3);
    display: flex; align-items: center; justify-content: center; text-align: center;
    font: 17px/21px "Oswald", sans-serif; color: var(--strip-red);
  }
  .front-author {
    height: 60px; display: flex; align-items: center; justify-content: center;
    font: 700 34px "Oxygen", sans-serif; color: var(--name-grey); letter-spacing: -1px;
    border-bottom: 2px solid #444;
  }
</style>
</head>
<body>
<main class="spread">
  <section class="back-cover">
    <header class="back-header">
      <div class="back-kicker">- Walking Out of Sorrow -</div>
      <div class="back-name"><small>DR.</small>NEIL PRENTOR</div>
    </header>
    <div class="back-body">
      <p>Millions of people feel the pain, loneliness, and agony of anxiety and depression every day. Many turn to Western medicine in the hopes that a pill will ease the pain and make the problem go away. Oftentimes, this only makes matters worse and doesn’t address the root cause. No one should have to struggle like this when natural answers exist that can address the physical, energetic, emotional, or spiritual causes of anxiety and depression. For 11 long years, Dr. Neil personally struggled with heavy depression until he discovered answers that helped him to completely heal. Walking Out of Sorrow is a guide that will help you discover - The two root physical causes of depression and exactly what to do to start healing today - How the negative emotions we have stored within from trauma and bad experiences can drive depression - Tools from Chinese medicine, applied kinesiology, and tapping to help you free your mind and live in peace - An actionable plan to help you let go of the pain, suffering, and negative emotions from your past. Whether you feel depressed and anxious or know someone who struggles with these issues, Walking Out of Sorrow will transform how you think about depression and will give you the tools to heal so that you can be free and live in peace.</p>
      <p><span class="author-portrait" role="img" aria-label="Portrait photo of the author"></span>Dr. Neil Prentor is a board-certified acupuncture physician licensed in the state of Florida. He received his training at the Marlow Institute of Holistic Practice. He also graduated with a master’s degree in counseling and psychology from Ashcombe Seminary of Theology. His mission is to help people transform their health and improve the quality of their life naturally. He lives in Orlando, FL where he runs a holistic medical clinic called Kestrel Wellness Center.<span class="author-site">www.drneilprentor.example</span></p>
    </div>
    <footer class="back-footer">
      <div class="social"><span class="social-mark"></span>drneilprentor</div>
      <div class="social"><span class="social-mark"></span>kestrelwellnesscenter</div>
    </footer>
  </section>

  <aside class="spine">
    <div class="spine-text">
      <span class="spine-author">DR. NEIL PRENTOR, AP, MA</span>
      <span class="spine-title">WALKING OUT OF SORROW</span>
    </div>
  </aside>

  <section class="front-cover">
    <header class="front-head">
      <h1 class="front-title">WALKING OUT OF SORROW</h1>
      <p class="front-subtitle">How To Use Tapping, Applied Kinesiology, &amp; Chinese Medicine<br>To Heal Your Body, Free Your Mind And Live In Peace</p>
    </header>
    <div class="front-art" role="img" aria-label="Illustration of a silhouetted figure with arms open above a city skyline, surrounded by flowers and sparks in warm orange tones">
      <span class="art-word art-emotional">EMOTIONAL</span>
      <span class="art-word art-learn">LEARN</span>
      <span class="art-word art-release">RELEASE</span>
      <span class="art-word art-freedom">FREEDOM</span>
      <span class="art-word art-healing">HEALING</span>
    </div>
    <p class="front-strip">Also Details My Own Personal Journey Of How I Was Able To Heal<br>From 11 Years Of Heavy Depression Through The Use Of These Tools</p>
    <div class="front-author">DR. NEIL PRENTOR, AP, MA</div>
  </section>
</main>
</body>
</html>
```